Business Card Design

Selling Televisions, Velorin, Kavo, Drelvatek, Morenzi
The latest models, sizes ranging from 22"- 75"
Surround Sounds, Sound Bars and Wall Mounts

Target Market(s)

Mainly males/boys/blokes etc

Industry/Entity Type

Business

Contact Information for Business Card

Glen Rudd
07812459306
glrudd@quillnetmail.com

Requirements
Must have
• simplistic design, probably just 2 of the images used

clarity essential
Nice to have
• Metallic if possible

```html
<!DOCTYPE html>
<html lang="en">
<head>
<meta charset="utf-8">
<title>Televisions – Glen Rudd Business Card</title>
<link href="https://fonts.googleapis.com/css2?family=Orbitron:wght@900&family=Open+Sans:ital,wght@0,400;0,600;0,700;1,400&display=swap" rel="stylesheet">
<style>
  :root {
    --stage: #2b2b2d;
    --silver-light: #e4e5e7;
    --silver-mid: #b9bbbe;
    --silver-dark: #8e9094;
    --band-black: #0b0b0c;
    --band-edge: #2a2a2c;
    --ink: #161617;
    --ink-soft: #4a4b4e;
    --text-light: #f2f2f2;
    --divider: #77797d;
  }
  * { box-sizing: border-box; margin: 0; padding: 0; }
  html, body { width: 1200px; height: 855px; overflow: hidden; }
  body {
    background: var(--stage);
    font-family: "Open Sans", Arial, sans-serif;
    position: relative;
  }
  .business-card {
    position: absolute;
    left: 75px; top: 127px;
    width: 1050px; height: 600px;
    border-radius: 38px;
    overflow: hidden;
    background: linear-gradient(160deg, var(--silver-light) 0%, var(--silver-mid) 45%, var(--silver-light) 70%, var(--silver-dark) 100%);
    box-shadow: 0 10px 30px rgba(0,0,0,.45);
  }
  .brand-title {
    position: absolute;
    right: 50px; top: 38px;
    font-family: "Orbitron", Arial, sans-serif;
    font-weight: 900;
    font-size: 68px;
    letter-spacing: 3px;
    color: var(--ink);
    line-height: 1;
  }
  .brand-tagline {
    position: absolute;
    right: 56px; top: 112px;
    font-size: 29px;
    color: var(--ink);
    line-height: 1;
  }
  .feature-band {
    position: absolute;
    left: 0; right: 0;
    top: 170px; height: 275px;
    background: linear-gradient(180deg, var(--band-edge) 0%, var(--band-black) 6%, var(--band-black) 94%, var(--band-edge) 100%);
  }
  .tv-screen {
    position: absolute;
    border: 4px solid #2e2f33;
    border-radius: 4px;
  }
  .tv-screen--lake {
    left: 55px; top: 22px; width: 290px; height: 190px;
    background: linear-gradient(180deg, #8f87a8 0%, #d9c6d3 45%, #6d6270 70%, #2f2b33 100%);
  }
  .tv-screen--city {
    right: 50px; top: 22px; width: 290px; height: 180px;
    background: linear-gradient(180deg, #3b3d78 0%, #7a5a9a 35%, #b0753f 65%, #3a2a38 100%);
  }
  .brand-list {
    position: absolute;
    left: 400px; top: 28px;
    list-style: none;
    color: var(--text-light);
    font-size: 27px;
    line-height: 34px;
    letter-spacing: 1px;
  }
  .brand-list li:nth-child(2) { padding-left: 22px; }
  .brand-list li:nth-child(3) { padding-left: 44px; }
  .brand-list li:nth-child(4) { padding-left: 66px; }
  .audio-line {
    position: absolute;
    left: 370px; top: 214px;
    color: var(--text-light);
    font-size: 24px;
    font-weight: 600;
    line-height: 32px;
    white-space: nowrap;
  }
  .contact-row {
    position: absolute;
    left: 70px; top: 478px;
    display: flex;
    align-items: center;
    gap: 26px;
  }
  .contact-name {
    font-size: 40px;
    font-weight: 700;
    color: var(--ink-soft);
    letter-spacing: 1px;
  }
  .contact-divider {
    width: 2px; height: 82px;
    background: var(--divider);
  }
  .contact-list { list-style: none; }
  .contact-item {
    display: flex; align-items: center; gap: 12px;
    font-size: 26px;
    color: var(--ink-soft);
    line-height: 40px;
  }
  .contact-icon { width: 24px; height: 24px; flex: none; }
</style>
</head>
<body>
  <article class="business-card">
    <h1 class="brand-title">TELEVISIONS</h1>
    <p class="brand-tagline">latest models sizes ranging from 22"-75"</p>

    <section class="feature-band">
      <div class="tv-screen tv-screen--lake" role="img" aria-label="Television showing a misty lake landscape at dusk"></div>
      <ul class="brand-list">
        <li>KAVO</li>
        <li>MORENZI</li>
        <li>VELORIN</li>
        <li>DRELVATEK</li>
      </ul>
      <p class="audio-line">Surround Sounds, Sound Bars and Wall Mounts</p>
      <div class="tv-screen tv-screen--city" role="img" aria-label="Television showing a city skyline at night"></div>
    </section>

    <footer class="contact-row">
      <p class="contact-name">GLEN RUDD</p>
      <span class="contact-divider"></span>
      <ul class="contact-list">
        <li class="contact-item">
          <svg class="contact-icon" viewBox="0 0 24 24" aria-hidden="true">
            <circle cx="12" cy="12" r="12" fill="#4a4b4e"/>
            <path d="M8.5 6.5c.6-.4 1.2-.2 1.5.3l1 1.8c.3.5.1 1-.3 1.3l-.6.4c.6 1.4 1.6 2.4 3 3l.4-.6c.3-.4.9-.6 1.3-.3l1.8 1c.5.3.7.9.3 1.5-.6 1-1.6 1.5-2.7 1.1-3-1-5.2-3.2-6.2-6.2-.3-1.1.1-2 .5-2.3z" fill="#e4e5e7"/>
          </svg>
          07812459306
        </li>
        <li class="contact-item">
          <svg class="contact-icon" viewBox="0 0 24 24" aria-hidden="true">
            <circle cx="12" cy="12" r="12" fill="#4a4b4e"/>
            <rect x="6" y="8" width="12" height="8" rx="1" fill="#e4e5e7"/>
            <path d="M6.5 8.5 12 12.5l5.5-4" stroke="#4a4b4e" stroke-width="1.2" fill="none"/>
          </svg>
          glrudd@quillnetmail.com
        </li>
      </ul>
    </footer>
  </article>
</body>
</html>
```